Email Signature

We are looking for creative email signature for our company. Please find attached the logo of our company for your reference. now we understand there isn't much can be done with email signature but we are looking for out of the box designs. Nothing specific in mind

Please insert fake numbers, website and/or address, etc just to showcase the designs. once the design is chosen we will provide the actual details.
Updates

Dear All,

We wouldlike to extend our apology for not being able to provide feedbacks to everysingle design. We were extremely busy and we have multiple contests opensimultaneously which makes the process harder. However, thank you all for theefforts you have put into this contest. We have received anoverwhelming quality responses & it has been a very difficult task tochoose just one, we easily Loved at least several designs...

Thanksagain for participating, we wish you all success in your design ventures.

Kindregards,

HLW Team

Industry/Entity Type

It Company

```html
<!DOCTYPE html>
<html lang="en">
<head>
<meta charset="utf-8">
<title>Email Signature – LanternWorks</title>
<link href="https://fonts.googleapis.com/css2?family=Open+Sans:ital,wght@0,400;0,700;0,800;1,400&display=swap" rel="stylesheet">
<style>
  :root {
    --ink: #333333;
    --brand-blue: #0f7fd8;
    --brand-green: #7dc31f;
    --frame-line: #6b6b6b;
    --paper: #ffffff;
  }
  html, body {
    margin: 0;
    padding: 0;
    overflow: hidden;
    background: var(--paper);
  }
  .signature {
    position: relative;
    width: 1200px;
    height: 1151px;
    overflow: hidden;
    background: var(--paper);
    font-family: "Open Sans", "Segoe UI", sans-serif;
  }
  .closing {
    position: absolute;
    left: 74px;
    top: 54px;
    margin: 0;
    font-size: 58px;
    font-weight: 400;
    color: var(--ink);
    line-height: 1;
  }
  .sender-name {
    position: absolute;
    left: 72px;
    top: 143px;
    margin: 0;
    font-size: 76px;
    font-weight: 700;
    color: var(--brand-blue);
    line-height: 1;
    letter-spacing: -0.5px;
  }
  .sender-role {
    position: absolute;
    left: 74px;
    top: 230px;
    margin: 0;
    font-size: 60px;
    font-style: italic;
    font-weight: 400;
    color: var(--ink);
    line-height: 1;
  }
  .wordmark {
    position: absolute;
    left: 60px;
    top: 350px;
    width: 1080px;
    height: 240px;
  }
  .wordmark text {
    font-family: "Open Sans", "Segoe UI", sans-serif;
    font-weight: 800;
    fill: var(--brand-blue);
  }
  .contact-row {
    position: absolute;
    left: 0;
    width: 1200px;
    height: 92px;
    font-size: 56px;
    line-height: 92px;
  }
  .contact-frame {
    position: absolute;
    top: 0;
    height: 92px;
    border: 2px solid var(--frame-line);
    border-radius: 30px;
    background: var(--paper);
    box-sizing: border-box;
  }
  .contact-label {
    position: absolute;
    right: 716px;
    top: 0;
    color: var(--brand-green);
  }
  .contact-value {
    position: absolute;
    left: 514px;
    top: 0;
    color: var(--brand-blue);
    white-space: nowrap;
  }
  .row-address { top: 616px; }
  .row-address .contact-frame { left: 240px; width: 882px; }
  .row-city { top: 710px; }
  .row-city .contact-frame { left: 324px; width: 822px; }
  .row-web { top: 803px; }
  .row-web .contact-frame { left: 306px; width: 780px; }
  .row-phone { top: 896px; }
  .row-phone .contact-frame { left: 366px; width: 714px; }
  .row-email { top: 990px; }
  .row-email .contact-frame { left: 282px; width: 828px; }
</style>
</head>
<body>
  <main class="signature">
    <p class="closing">Best regards,</p>
    <p class="sender-name">Name Surname</p>
    <p class="sender-role">general manager</p>

    <svg class="wordmark" viewBox="0 0 1080 240" role="img" aria-label="LanternWorks">
      <text x="540" y="182" font-size="176" text-anchor="middle" textLength="1040" lengthAdjust="spacingAndGlyphs">LanternWorks</text>
    </svg>

    <div class="contact-row row-address">
      <div class="contact-frame"></div>
      <span class="contact-label">Adress:</span>
      <span class="contact-value">Street name, no.01</span>
    </div>
    <div class="contact-row row-city">
      <div class="contact-frame"></div>
      <span class="contact-label">City:</span>
      <span class="contact-value">Anytown, NY 12345</span>
    </div>
    <div class="contact-row row-web">
      <div class="contact-frame"></div>
      <span class="contact-label">Web:</span>
      <span class="contact-value">www.website.com</span>
    </div>
    <div class="contact-row row-phone">
      <div class="contact-frame"></div>
      <span class="contact-label">Tel:</span>
      <span class="contact-value">+1 500 90 80 555</span>
    </div>
    <div class="contact-row row-email">
      <div class="contact-frame"></div>
      <span class="contact-label">Email:</span>
      <span class="contact-value">info@website.com</span>
    </div>
  </main>
</body>
</html>
```